Business Card Design Project

Business Card
We are rebranding with a new logo
Industry/Entity Type
Business
Contact Information for Business Card
Dennis Marlow +61 427581962 dennis@qovo.com.au P.O. Box 872 Kelvindale QLD 4309
Requirements
Must have
- Logo

```html
<!DOCTYPE html>
<html lang="en">
<head>
<meta charset="utf-8">
<title>Qovo International – Business Card</title>
<link href="https://fonts.googleapis.com/css2?family=Open+Sans:wght@300;400;600&display=swap" rel="stylesheet">
<style>
  :root {
    --page-bg: #e9e6e2;
    --card-top: #f1efed;
    --card-top-shade: #dcd9d6;
    --rule-dark: #4a4d52;
    --band-light: #4fb2f3;
    --band-mid: #2f98ec;
    --band-deep: #2a7fe0;
    --pattern-tone: #3f8ee6;
    --text-white: #ffffff;
    --title-ink: #24466e;
    --brand-ink: #263a52;
  }
  * { margin: 0; padding: 0; box-sizing: border-box; }
  html, body {
    width: 1200px;
    height: 686px;
    overflow: hidden;
    background: var(--page-bg);
    font-family: "Open Sans", Arial, sans-serif;
  }
  .canvas {
    position: relative;
    width: 1200px;
    height: 686px;
  }
  .card {
    position: absolute;
    left: 100px;
    top: 85px;
    width: 1000px;
    height: 515px;
    border-radius: 14px;
    overflow: hidden;
    box-shadow: 0 6px 24px rgba(0,0,0,0.12);
  }
  .card-header {
    position: absolute;
    left: 0; top: 0;
    width: 100%;
    height: 221px;
    background: linear-gradient(180deg, var(--card-top) 0%, var(--card-top-shade) 100%);
    display: flex;
    align-items: center;
    justify-content: center;
  }
  .brand {
    display: flex;
    flex-direction: column;
    align-items: center;
    color: var(--brand-ink);
    font-weight: 600;
    line-height: 1;
  }
  .brand-name {
    font-size: 86px;
    letter-spacing: 2px;
  }
  .brand-sub {
    margin-top: 16px;
    font-size: 24px;
    letter-spacing: 4px;
  }
  .header-rule {
    position: absolute;
    left: 0; top: 221px;
    width: 100%;
    height: 6px;
    background: var(--rule-dark);
  }
  .contact-band {
    position: absolute;
    left: 0; top: 227px;
    width: 100%;
    height: 288px;
    background: linear-gradient(180deg, var(--band-light) 0%, var(--band-mid) 55%, var(--band-deep) 100%);
  }
  .band-pattern {
    position: absolute;
    left: 0; bottom: 0;
    width: 100%;
    height: 200px;
    background: linear-gradient(180deg, rgba(63,142,230,0) 0%, rgba(63,142,230,0.35) 60%, rgba(40,110,215,0.45) 100%);
  }
  .person {
    position: absolute;
    left: 46px;
    top: 88px;
    color: var(--text-white);
  }
  .person-name {
    font-size: 52px;
    font-weight: 400;
    letter-spacing: 1px;
    line-height: 1;
    white-space: nowrap;
  }
  .person-title {
    margin-top: 8px;
    margin-left: 140px;
    font-size: 34px;
    font-weight: 400;
    letter-spacing: 4px;
    color: var(--title-ink);
    line-height: 1;
  }
  .band-divider {
    position: absolute;
    left: 488px;
    top: 22px;
    width: 3px;
    height: 250px;
    background: var(--text-white);
  }
  .contact-list {
    position: absolute;
    left: 508px;
    top: 34px;
    list-style: none;
    color: var(--text-white);
  }
  .contact-item {
    display: flex;
    align-items: center;
    height: 36px;
    margin-bottom: 21px;
    font-size: 23px;
    letter-spacing: 1.5px;
    white-space: nowrap;
  }
  .contact-icon {
    width: 32px;
    height: 32px;
    margin-right: 22px;
    flex: none;
  }
</style>
</head>
<body>
<div class="canvas">
  <div class="card">
    <div class="card-header">
      <div class="brand">
        <span class="brand-name">QOVO</span>
        <span class="brand-sub">INTERNATIONAL</span>
      </div>
    </div>
    <div class="header-rule"></div>
    <div class="contact-band">
      <div class="band-pattern" role="img" aria-label="Faint blue diamond pattern across the lower band"></div>
      <div class="person">
        <div class="person-name">Dennis Marlow</div>
        <div class="person-title">C.E.O</div>
      </div>
      <div class="band-divider"></div>
      <ul class="contact-list">
        <li class="contact-item">
          <svg class="contact-icon" viewBox="0 0 32 32" aria-hidden="true">
            <rect x="9" y="3" width="14" height="26" rx="2.5" fill="none" stroke="#fff" stroke-width="2.6"/>
            <line x1="14" y1="25" x2="18" y2="25" stroke="#fff" stroke-width="2"/>
          </svg>
          +61 427 581962
        </li>
        <li class="contact-item">
          <svg class="contact-icon" viewBox="0 0 32 32" aria-hidden="true">
            <g fill="none" stroke="#fff" stroke-width="2">
              <circle cx="16" cy="16" r="12"/>
              <ellipse cx="16" cy="16" rx="5.5" ry="12"/>
              <line x1="4" y1="16" x2="28" y2="16"/>
              <path d="M6 10 H26 M6 22 H26"/>
            </g>
          </svg>
          www.qovo.com.au
        </li>
        <li class="contact-item">
          <svg class="contact-icon" viewBox="0 0 32 32" aria-hidden="true">
            <rect x="3" y="7" width="26" height="18" fill="#fff"/>
            <path d="M3 7 L16 18 L29 7" fill="none" stroke="#2f98ec" stroke-width="2.2"/>
            <path d="M3 25 L12 15 M29 25 L20 15" fill="none" stroke="#2f98ec" stroke-width="1.8"/>
          </svg>
          dennis@qovo.com.au
        </li>
        <li class="contact-item">
          <svg class="contact-icon" viewBox="0 0 32 32" aria-hidden="true">
            <path d="M16 3 C10 3 6.5 7.5 6.5 12.5 C6.5 19 16 29 16 29 C16 29 25.5 19 25.5 12.5 C25.5 7.5 22 3 16 3 Z" fill="#fff"/>
            <circle cx="16" cy="12.5" r="3.8" fill="#2f98ec"/>
          </svg>
          P.O. Box 872 Kelvindale QLD 4309
        </li>
      </ul>
    </div>
  </div>
</div>
</body>
</html>
```